Create a Graphic About YOURSELF and PixelHarbor

PixelHarbor would like you (designers) to create an awesome graphic to promote YOURSELF and your profile on PixelHarbor!

Your graphic should communicate your name, your services and should mention PixelHarbor.

The design should be perfect for sharing on Chatterly. Here's an example of what we'd like http://blog.pixelharbor-example.ca/article/333/pixelharbor-launches-3000-hire-me-social-design-contest

Once you submitted your design, we'd love you to share the design ('advertisement') and promote yourself and PixelHarbor to your friends and potential customers. So make your submissions great and get your friends to vote for your design by 'Liking' it on Chatterly!

Prizes:
$1500 - "PixelHarbor Community" prize awarded to the designer with the most Chatterly 'Likes'
5 x $50 for the next 5 'most liked' designs on Chatterly

$1000 - "Hire Me" prize awarded to the designer who receives the most client invites
5 x $50 for the next 5 'most invited' designers

In summary, this is a great opportunity for you to increase your exposure to PixelHarbor customers and win cash prizes. Show off your design skills and get hired by PixelHarbor customers from around the world!

Target Market(s)

Fans, friends and customers of YOU

Industry/Entity Type

Cash

Requirements
Must have
• 1) Include your PixelHarbor user name on the graphic so customers can find you in the PixelHarbor Designer Directory
2) Include the tagline "Hire Me on PixelHarbor.com!" in your graphic design.
3) Share your design's URL on our Chatterly wall at http://chatterly-example.com/pixelharbor and get your friends to 'like' your design.
Nice to have
• 1) Include a tagline that expresses your design approach/philosophy
2) Artwork dimensions: 403 x 403 px
3) You can submit more than 1 design!
Should not have
• You must own the copyright of any images you use including stock imagery.

```html
<!DOCTYPE html>
<html lang="en">
<head>
<meta charset="utf-8">
<title>Hire Me on PixelHarbor.com!</title>
<link rel="stylesheet" href="https://fonts.googleapis.com/css2?family=Archivo+Black&family=Bowlby+One&family=Arimo:wght@400;700&display=swap">
<style>
  :root {
    --bg-light: #d6d6d6;
    --bg-mid: #a4a4a4;
    --bg-dark: #666666;
    --ink: #0d0d0d;
    --accent: #f7c300;
    --lettering: #f2c21b;
    --brand-ink: #3a3a3a;
    --brand-dot: #1f6f93;
  }
  html, body {
    margin: 0;
    padding: 0;
    width: 1200px;
    height: 982px;
    overflow: hidden;
  }
  .promo {
    position: relative;
    width: 1200px;
    height: 982px;
    background: linear-gradient(100deg, var(--bg-light) 0%, var(--bg-mid) 45%, var(--bg-dark) 100%);
  }
  .promo svg { display: block; }
  .headline { font-family: "Archivo Black", sans-serif; }
  .headline-ink { fill: var(--ink); }
  .headline-accent { fill: var(--accent); }
  .role { font-family: "Bowlby One", sans-serif; fill: var(--lettering); }
  .role-mark { font-family: "Bowlby One", sans-serif; fill: #1e1e1e; }
  .hire-label { font-family: "Arimo", sans-serif; fill: #111; letter-spacing: 1px; }
  .brand-name { font-family: "Arimo", sans-serif; fill: var(--brand-ink); }
  .brand-dot { fill: var(--brand-dot); }
  .brand-url { font-family: "Arimo", sans-serif; fill: #111; letter-spacing: 2.5px; }
  .username { font-family: "Arimo", sans-serif; font-weight: 700; fill: var(--accent); }
</style>
</head>
<body>
<main class="promo">
  <svg width="1200" height="982" viewBox="0 0 1200 982" xmlns="http://www.w3.org/2000/svg">
    <defs>
      <linearGradient id="portrait-tone" x1="0" y1="0" x2="1" y2="0">
        <stop offset="0" stop-color="#111" stop-opacity="0.9"/>
        <stop offset="0.7" stop-color="#222" stop-opacity="0.75"/>
        <stop offset="1" stop-color="#555" stop-opacity="0"/>
      </linearGradient>
    </defs>

    <rect class="designer-portrait" x="0" y="0" width="650" height="982" fill="url(#portrait-tone)"
          role="img" aria-label="Stylised black silhouette portrait of the designer in a t-shirt"/>

    <text class="headline headline-ink" x="1096" y="147" text-anchor="end" font-size="140">ARE YOU</text>
    <text class="headline headline-accent" x="1096" y="249" text-anchor="end" font-size="110">LOOKING</text>
    <text class="headline headline-ink" x="1096" y="327" text-anchor="end" font-size="76">FOR A</text>

    <text class="role" x="584" y="453" font-size="70" textLength="409" lengthAdjust="spacingAndGlyphs">GRAPHIC</text>
    <text class="role" x="584" y="529" font-size="76" textLength="436" lengthAdjust="spacingAndGlyphs">DESIGNER</text>
    <text class="role-mark" x="1066" y="532" text-anchor="middle" font-size="190">?</text>

    <text class="hire-label" x="1096" y="698" text-anchor="end" font-size="30">Hire me at:</text>

    <circle class="brand-dot" cx="731" cy="775" r="20"/>
    <text class="brand-name" x="1096" y="792" text-anchor="end" font-size="47">PixelHarbor</text>
    <text class="brand-url" x="1096" y="838" text-anchor="end" font-size="27">www.pixelharbor.com</text>

    <text class="username" x="1096" y="931" text-anchor="end" font-size="62">novaline207</text>
  </svg>
</main>
</body>
</html>
```